依頼詳細
当店一品料理での一番人気商品「炭焼き月白鶏」を常温仕様で作成し、通信販売、ギフト等に活用できるようにと思います。
記載項目
サイズ 縦12cm×横20cm×高さ3cmの半透明のプラスチック箱の内側にミラー紙180kの紙を差込みます。(紙は縦15cm×横20cmで縦15cmの上部3cmは上面に折ります。
その紙のデザインを希望いたします。
文字は (一味ちがう  「炭焼き月白鶏」)と(月白亭)を入れる予定です。
オリーブを連想できるような色を希望いたします。
希望イメージ
シンプル 複雑
単色 カラフル
暗い 明るい
日常 高級
遊び心 厳粛
未来的 伝統的
女性的 男性的
希望する色
緑系
納品ファイル
• 高解像度JPG (.jpg)
補足説明
■ 選んだ理由

思いつかないような素晴らしいデザインで有難うございました。とても満足致しております。
今後とも何卒宜しくお願い致します。

■ 提案者全員のお礼・コメント

お忙しい中数多くのご提案を頂きまして有難うございました。
今後とも何卒宜しくお願い致します。

```html
<!DOCTYPE html>
<html lang="ja">
<head>
<meta charset="utf-8">
<title>炭焼き月白鶏 パッケージ差込紙</title>
<link rel="stylesheet" href="https://fonts.googleapis.com/css2?family=Yuji+Syuku&display=swap">
<style>
  :root {
    --paper: #ffffff;
    --linen: #dde7d3;
    --linen-deep: #cfdcc3;
    --linen-edge: #b5c6a7;
    --olive-green: #3d8a4f;
    --olive-dark: #2c6b3b;
    --fold-line: #a3b596;
    --ink: #111111;
    --accent-red: #d0201c;
  }
  * { margin: 0; padding: 0; box-sizing: border-box; }
  html, body { width: 846px; height: 1200px; overflow: hidden; background: var(--paper); }
  .canvas { position: relative; width: 846px; height: 1200px; }

  .insert-sheet {
    position: absolute; left: 14px; top: 192px; width: 812px; height: 603px;
    background: radial-gradient(ellipse at center, var(--linen) 55%, var(--linen-deep) 100%);
    border: 1px solid var(--linen-edge);
  }
  .fold-line {
    position: absolute; left: 0; right: 0; top: 96px; height: 0;
    border-top: 1px solid var(--fold-line);
  }

  .lid-band {
    position: absolute; left: 85px; top: 22px; width: 662px; height: 62px;
    background: var(--paper);
    border: 4px double var(--olive-green);
    display: flex; align-items: center; padding: 0 22px;
  }
  .tagline, .product-name, .shop-name { font-family: "Yuji Syuku", serif; }
  .lid-band .tagline { color: var(--accent-red); font-size: 20px; letter-spacing: 4px; }
  .lid-band .product-name { color: var(--ink); font-size: 38px; margin-left: 26px; letter-spacing: 2px; }
  .lid-band .shop-mark { margin-left: auto; }

  .front-panel {
    position: absolute; left: 76px; top: 169px; width: 657px; height: 358px;
    background: var(--paper);
    border: 5px double var(--olive-green);
    outline: 1px solid var(--olive-green);
    outline-offset: -14px;
  }
  .frame-corners { position: absolute; inset: 0; width: 100%; height: 100%; }
  .front-panel .tagline {
    position: absolute; left: 0; right: 0; top: 54px; text-align: center;
    color: var(--accent-red); font-size: 32px; letter-spacing: 8px; padding-right: 150px;
  }
  .front-panel .product-name {
    position: absolute; left: 0; right: 0; top: 108px; text-align: center;
    color: var(--ink); font-size: 82px; letter-spacing: 4px;
  }
  .front-panel .shop-mark {
    position: absolute; left: 0; right: 0; top: 240px;
    display: flex; justify-content: center; align-items: center;
  }
  .shop-mark { display: flex; align-items: center; gap: 8px; }
  .shop-dot { width: 14px; height: 14px; border-radius: 50%; background: var(--olive-green); }
  .shop-name { color: var(--olive-green); font-size: 26px; letter-spacing: 4px; }
  .front-panel .shop-name { font-size: 44px; }
  .front-panel .shop-dot { width: 22px; height: 22px; }
</style>
</head>
<body>
<div class="canvas">
  <section class="insert-sheet">
    <div class="lid-band">
      <span class="tagline">一味ちがう</span>
      <span class="product-name">炭焼き月白鶏</span>
      <span class="shop-mark"><span class="shop-dot"></span><span class="shop-name">月白亭</span></span>
    </div>
    <div class="fold-line"></div>

    <div class="front-panel">
      <svg class="frame-corners" viewBox="0 0 647 348" preserveAspectRatio="none" aria-hidden="true">
        <g fill="none" stroke="#3d8a4f" stroke-width="2">
          <path d="M14 40 H40 V14"/>
          <path d="M633 40 H607 V14"/>
          <path d="M14 308 H40 V334"/>
          <path d="M633 308 H607 V334"/>
        </g>
      </svg>
      <p class="tagline">一味ちがう</p>
      <h1 class="product-name">炭焼き月白鶏</h1>
      <div class="shop-mark"><span class="shop-dot"></span><span class="shop-name">月白亭</span></div>
    </div>
  </section>
</div>
</body>
</html>
```